CBD Boutique Business Card Needed

We are in need of a business card to reflect the direction of our latest products. We are a fully organic company in which our store and products are very heavy in wood and "natural" components. We decided to bring color into one of our brands and immediately knew this is where we needed to go.

We are NOT a cash grab CBD company. We could have done this wrong, slapped a label on a shit product and left it like that. I am passionate about sharing my experience with other veterans and opening a store and making it a comfortable place for others to come and see if they can have the same experience.

Target Market(s)

We are a dual market company. We do have a beauty line that will cover the costs of the majority of our business. But we also heavily cater to veterans and first responders. I am a veteran and this is how I found out about CBD. So the marketing needs to bring in our higher end beauty clientele but also be able to not put off our customers that readily need this.

Contact Information for Business Card

What we are looking for is a light, professional, boutique design that is is neither quite feminine or masculine. Attached is a picture of a store in Portland that we asked our store designer to get her inspiration from. But all natural wood and black outlines are what is mostly in there.

Attached are the following files:

Logo: An AI file with how we have our logo. I do not understand AI and have no idea why the letters are individual. The font is Adam. OLU is the logo and Tonics of Vigor is our tagline.

KM Vantage (front and back) cards I did originally found at a trade show that I absolutely loved...while it is mostly there and I would still be happy with them but it is me pretending to be you. I understand I am not and there is probably a lot wrong that all of you would see instantly and this is why I am here.

Dropper Bottle: This is our final product mock up

Water Color: I am semi flexible here. This water color is slightly different on every level of our brand. The color itself can change...we are not stuck on THIS particular one. If you happen to make a new one that is similar in style and we use it...then I will happily commission you to change the rest on our next product run. I am pretty sure you can use this statement as evidence later . =) .

But seriously, we heavily believe in pay it forward and will work with anyone here that may have a vision bigger than ours. The winner of this contest will get preferential consideration on our marketing materials (need letterhead etc. next, as well as a brochure, and website) so three more projects coming down the pipeline.

Information to use for your mockup is contained on the card images I have included. I would prefer CBD for wellness CBD for life to be more prominent. No where else on the card do we have CBD mentioned.

Font styles to use
Sans Serif

Colors

Designer to choose colors to be used in the design.

Requirements
Must have
• Double Sided
• Front: OLU logo on front of card will be raised embossed. Background is watercolor. One has been provided. Others are up for consideration. If the rest of your design is incredible and I don't like your watercolor I will just ask to swap it.
• Back: Standard information. Not stuck on anything here. I LOVE clean minimal designs. The bleed on the card I provided is a luxury...
• Font for title and OLU is Adam. Everything else I prefer san serif or as clean as possible.
Nice to have
• I Need to incorporate Calmly Replenishing somewhere on the card. Bold but not intrusive.

```html
<!DOCTYPE html>
<html lang="en">
<head>
<meta charset="utf-8">
<title>OLU Tonics of Vigor – Business Card</title>
<link href="https://fonts.googleapis.com/css2?family=Lato:wght@100;300;400&display=swap" rel="stylesheet">
<style>
  :root {
    --page: #ffffff;
    --card: #ffffff;
    --card-edge: #9a9a9a;
    --ink: #1e1e1e;
    --ink-soft: #6f6f6f;
    --ink-faint: #8a8a8a;
    --wash-blue: rgba(98, 189, 214, 0.8);
    --wash-teal: rgba(120, 200, 205, 0.6);
    --wash-green: rgba(178, 210, 120, 0.65);
    --wash-lime: rgba(205, 225, 150, 0.5);
  }
  * { box-sizing: border-box; margin: 0; padding: 0; }
  html, body {
    width: 1200px; height: 1200px; overflow: hidden;
    background: var(--page);
    font-family: "Lato", Arial, sans-serif;
    color: var(--ink);
  }
  .canvas { position: relative; width: 1200px; height: 1200px; }

  .card {
    position: absolute;
    background: var(--card);
    border: 2px solid var(--card-edge);
    overflow: hidden;
  }
  .card--front { left: 159px; top: 27px; width: 927px; height: 507px; }
  .card--back  { left: 240px; top: 675px; width: 927px; height: 459px; }

  /* Watercolour washes */
  .wash { position: absolute; filter: blur(10px); }
  .wash--front {
    left: 80px; top: 10px; width: 770px; height: 480px;
    background:
      radial-gradient(ellipse 42% 40% at 62% 36%, var(--wash-blue), transparent 78%),
      radial-gradient(ellipse 32% 38% at 80% 30%, var(--wash-teal), transparent 78%),
      radial-gradient(ellipse 36% 36% at 26% 62%, var(--wash-green), transparent 78%),
      radial-gradient(ellipse 28% 28% at 16% 76%, var(--wash-lime), transparent 78%),
      radial-gradient(ellipse 48% 40% at 50% 66%, rgba(150, 205, 190, 0.45), transparent 78%);
  }
  .wash--back {
    right: -80px; top: -60px; width: 700px; height: 580px;
    background:
      radial-gradient(ellipse 46% 40% at 76% 24%, var(--wash-blue), transparent 78%),
      radial-gradient(ellipse 42% 46% at 56% 46%, var(--wash-teal), transparent 78%),
      radial-gradient(ellipse 38% 40% at 38% 74%, var(--wash-green), transparent 78%),
      radial-gradient(ellipse 30% 30% at 62% 88%, var(--wash-lime), transparent 78%);
  }

  /* Front */
  .brand {
    position: absolute; left: 0; right: 0; top: 160px;
    text-align: center;
  }
  .brand__name {
    font-weight: 300;
    font-size: 178px;
    line-height: 1;
    letter-spacing: 12px;
    color: var(--ink);
  }
  .brand__tagline {
    margin-top: 10px;
    font-weight: 400;
    font-size: 30px;
    letter-spacing: 1px;
    text-transform: uppercase;
    color: var(--ink);
  }
  .motto {
    position: absolute; left: 0; right: 0; top: 440px;
    text-align: center;
    font-weight: 300;
    font-size: 20px;
    letter-spacing: 13px;
    color: var(--ink-faint);
  }

  /* Back */
  .contact { position: absolute; left: 42px; top: 76px; list-style: none; }
  .contact__item {
    position: absolute; left: 0; width: 320px;
    display: flex; align-items: center;
  }
  .contact__item--address { top: 0; }
  .contact__item--phone   { top: 110px; }
  .contact__item--email   { top: 180px; }
  .contact__item--web     { top: 255px; }
  .contact__icon { width: 32px; height: 32px; flex: none; fill: var(--ink); }
  .contact__text {
    margin-left: 34px;
    font-weight: 300;
    font-size: 20px;
    line-height: 1.15;
    color: var(--ink-soft);
  }
  .person {
    position: absolute; right: 150px; top: 196px;
    text-align: right;
  }
  .person__name {
    font-weight: 400; font-size: 47px; color: var(--ink); line-height: 1.1;
  }
  .person__role {
    margin-top: 4px;
    font-weight: 300; font-size: 20px; letter-spacing: 1px; color: var(--ink-soft);
  }
</style>
</head>
<body>
<main class="canvas">

  <section class="card card--front" aria-label="Card front">
    <div class="wash wash--front" role="img" aria-label="Blue and green watercolour wash"></div>
    <div class="brand">
      <h1 class="brand__name">OLU</h1>
      <p class="brand__tagline">Tonics of Vigor</p>
    </div>
    <p class="motto">Calmly Replenishing</p>
  </section>

  <section class="card card--back" aria-label="Card back">
    <div class="wash wash--back" role="img" aria-label="Blue and green watercolour wash"></div>

    <ul class="contact">
      <li class="contact__item contact__item--address">
        <svg class="contact__icon" viewBox="0 0 24 24" aria-hidden="true">
          <path d="M12 1.5a7.5 7.5 0 0 0-7.5 7.5c0 5.6 7.5 13.5 7.5 13.5s7.5-7.9 7.5-13.5A7.5 7.5 0 0 0 12 1.5zm0 10.5a3 3 0 1 1 0-6 3 3 0 0 1 0 6z"/>
        </svg>
        <span class="contact__text">4120 N Alder Ridge Rd<br>Mesa, AZ 85201<br>Suite 200</span>
      </li>
      <li class="contact__item contact__item--phone">
        <svg class="contact__icon" viewBox="0 0 24 24" aria-hidden="true">
          <path d="M6.6 10.8a15.1 15.1 0 0 0 6.6 6.6l2.2-2.2a1 1 0 0 1 1-.25 11.4 11.4 0 0 0 3.6.57 1 1 0 0 1 1 1V20a1 1 0 0 1-1 1A17 17 0 0 1 3 4a1 1 0 0 1 1-1h3.5a1 1 0 0 1 1 1c0 1.250.2 2.45.57 3.57a1 1 0 0 1-.25 1z"/>
        </svg>
        <span class="contact__text">480.217.4390</span>
      </li>
      <li class="contact__item contact__item--email">
        <svg class="contact__icon" viewBox="0 0 24 24" aria-hidden="true">
          <rect x="1.5" y="5" width="21" height="14" rx="1"/>
        </svg>
        <span class="contact__text">hello@olu.life</span>
      </li>
      <li class="contact__item contact__item--web">
        <svg class="contact__icon" viewBox="0 0 24 24" aria-hidden="true">
          <circle cx="12" cy="12" r="10.5"/>
          <path d="M1.5 12h21M12 1.5c3 3 3 18 0 21M12 1.5c-3 3-3 18 0 21" stroke="#fff" stroke-width="1.2" fill="none"/>
        </svg>
        <span class="contact__text">www.olu.life</span>
      </li>
    </ul>

    <div class="person">
      <h2 class="person__name">Dana Whitfield</h2>
      <p class="person__role">OWNER / CEO</p>
    </div>
  </section>

</main>
</body>
</html>
```